Vexora.app is a developing company for entrepreneurs who need legal services.

Our Company Slogan is : The Only Path You Want
Company Info:
Vexora is built to help anyone sort through the confusion of taking an idea from thoughts to a tangible reality, legally. We are here to help make the incorporation, idea protection and any other legal necessities an after thought for you. If you know your idea is the next Pindleco we will help you make the right legal decisions from the start.
Subscription Model packages: 2.99, 4.99, 9.99 options in three separate boxes. Choose a monthly option and get started with your startups legal services. Start Now!
Follow us on Social: @vexora.app
Website template look:
Build an app landing page for the company. Need a clean subscription based template with my updated logo and color scheme to create a landing page, team, and contact page. I want to be able to edit the copy. Very simple and clean using company colors.
Target Market(s)
Gen-Z or Millenial aged entrepreneurs starting a business for the first time.
Industry/Entity Type
Legal
Coding
Coded - Design and coding required
Number of Pages Required
3 page
Font styles to use
Other font styles liked:
- Roboto, or Museo Sans 300,700
Look and feel

```html
<!DOCTYPE html>
<html lang="en">
<head>
<meta charset="utf-8">
<title>Vexora — The Only Path You Want</title>
<link rel="stylesheet" href="https://fonts.googleapis.com/css2?family=Roboto:wght@300;400;500;700&display=swap">
<style>
:root{
  --blue:#3fb1f2;
  --green:#95c94a;
  --ink:#222;
  --text:#444;
  --muted:#666;
  --grey-bg:#ececec;
  --dark:#2a2a2a;
  --white:#fff;
}
*{box-sizing:border-box;margin:0;padding:0}
html,body{width:1200px;height:4286px;overflow:hidden}
body{font-family:'Roboto',sans-serif;color:var(--text);background:var(--white);position:relative}
a{color:inherit;text-decoration:none}

/* header */
.site-header{position:absolute;top:0;left:0;width:1200px;height:140px;background:var(--white)}
.brand{position:absolute;left:110px;top:70px;display:flex;align-items:center;gap:10px}
.brand-mark{width:34px;height:34px;border-radius:50%;background:var(--blue)}
.brand-name{font-size:30px;font-weight:700;color:var(--blue);letter-spacing:1px}
.contact-item{position:absolute;top:20px;display:flex;gap:10px;align-items:flex-start}
.contact-item small{display:block;font-size:14px;color:var(--ink)}
.contact-item strong{display:block;font-size:18px;font-weight:500;color:var(--green)}
.main-nav{position:absolute;top:96px;left:529px}
.main-nav a{position:absolute;font-size:18px;color:var(--ink);white-space:nowrap}
.main-nav a.active{color:var(--blue);text-decoration:underline}

/* hero */
.hero{position:absolute;top:140px;left:0;width:1200px;height:514px;
  background:linear-gradient(110deg,#2f7fc0 0%,#3a9ab8 30%,#7fbf4a 52%,#4a5560 70%,#2c3440 100%)}
.hero h1{position:absolute;left:110px;top:128px;font-size:56px;font-weight:700;color:var(--white)}
.hero p{position:absolute;left:110px;top:212px;width:500px;font-size:24px;font-weight:300;line-height:34px;color:var(--white)}
.btn-outline{position:absolute;left:112px;top:323px;width:118px;height:58px;border:2px solid var(--white);border-radius:3px;color:var(--white);font-size:17px;display:flex;align-items:center;justify-content:center}

/* about */
.about{position:absolute;top:654px;left:0;width:1200px;height:547px}
.section-title{font-size:46px;font-weight:700}
.section-title .b{color:var(--blue)}
.section-title .g{color:var(--green)}
.about .section-title{position:absolute;left:110px;top:92px}
.about h3{position:absolute;left:112px;top:162px;font-size:28px;font-weight:500;color:var(--ink)}
.about p{position:absolute;left:112px;width:518px;font-size:17px;line-height:28px;text-align:justify;color:var(--text)}
.btn{position:absolute;height:56px;color:var(--white);font-size:18px;display:flex;align-items:center;justify-content:center;border-radius:3px}
.btn.blue{background:var(--blue)}
.btn.green{background:var(--green)}
.about-art{position:absolute;left:660px;top:70px;width:540px;height:477px;background:radial-gradient(circle at 50% 55%,#f2f2f2,#ffffff 75%)}

/* services */
.services{position:absolute;top:1201px;left:0;width:1200px;height:767px;background:linear-gradient(135deg,#e2e2e2,#f1f1f1 50%,#e4e4e4)}
.vertical-title{position:absolute;left:30px;top:590px;transform:rotate(-90deg);transform-origin:left top;font-size:48px;font-weight:700;white-space:nowrap}
.tablet{position:absolute;left:120px;top:88px;width:312px;height:470px;background:var(--white);border-radius:22px;box-shadow:0 4px 14px rgba(0,0,0,.12)}
.tablet-screen{position:absolute;left:12px;top:45px;width:288px;height:380px;background:linear-gradient(160deg,#8dcb50,#3fb1f2);display:flex;align-items:center;justify-content:center}
.tablet-screen span{font-size:40px;font-weight:700;color:var(--white);letter-spacing:1px}
.phone{position:absolute;left:378px;top:192px;width:188px;height:390px;background:var(--white);border-radius:20px;box-shadow:0 4px 14px rgba(0,0,0,.14)}
.phone-screen{position:absolute;left:10px;top:40px;width:168px;height:310px;background:linear-gradient(180deg,#44505c 0 25%,#f6f6f6 25% 55%,#d9dee2 55%)}
.card{position:absolute;left:658px;width:377px;height:180px;background:var(--white);box-shadow:0 3px 10px rgba(0,0,0,.12)}
.card svg{position:absolute;left:30px;top:30px}
.card h4{position:absolute;left:107px;top:28px;font-size:23px;font-weight:500;color:var(--ink)}
.card p{position:absolute;left:107px;top:70px;width:245px;font-size:17px;line-height:22px;color:var(--text)}
.card a{position:absolute;left:107px;font-size:16px;color:var(--blue)}

/* pricing */
.pricing{position:absolute;top:1968px;left:0;width:1200px;height:820px}
.pricing .section-title{position:absolute;left:0;width:1200px;top:80px;text-align:center}
.pricing .lead{position:absolute;left:130px;width:940px;top:152px;text-align:center;font-size:17px;line-height:28px;color:var(--ink)}
.plan{position:absolute;background:var(--white);box-shadow:0 4px 16px rgba(0,0,0,.08);text-align:center}
.plan-head{height:74px;display:flex;align-items:center;justify-content:center;color:var(--white);font-size:22px;font-weight:500}
.plan .price{font-size:34px;font-weight:700;margin-top:36px}
.plan ul{list-style:none;margin-top:20px;font-size:15px;line-height:25px;color:var(--text)}
.plan .cta{display:inline-flex;margin-top:28px;height:58px;padding:0 20px;align-items:center;color:var(--white);font-size:20px;font-weight:500}
.plan.silver,.plan.platinum{top:284px;width:304px;height:418px}
.plan.silver .plan-head,.plan.platinum .plan-head,.plan.silver .cta,.plan.platinum .cta{background:var(--blue)}
.plan.silver .price,.plan.platinum .price{color:var(--blue)}
.plan.gold{top:262px;left:415px;width:370px;height:460px;z-index:2}
.plan.gold .plan-head{height:82px;background:var(--green)}
.plan.gold .price{color:var(--green);font-size:42px}
.plan.gold ul{font-size:17px;line-height:28px}
.plan.gold .cta{background:var(--green)}

/* stats */
.stats{position:absolute;top:2788px;left:0;width:1200px;height:536px;background:linear-gradient(100deg,#1d5f8e 0%,#2d6f95 40%,#4f8a55 75%,#6a9a3a 100%)}
.stats h2{position:absolute;left:108px;top:110px;font-size:46px;font-weight:700;color:var(--white)}
.stats .intro{position:absolute;left:111px;top:175px;width:640px;font-size:17px;line-height:28px;color:var(--white)}
.stats .count{position:absolute;left:108px;top:250px;font-size:76px;font-weight:700;color:var(--white)}
.stats .outro{position:absolute;left:111px;top:376px;width:640px;font-size:20px;line-height:33px;color:var(--white)}
.stats-badge{position:absolute;left:790px;top:120px;width:290px;height:290px;border-radius:50%;background:var(--blue);display:flex;align-items:center;justify-content:center}
.stats-badge span{font-size:44px;font-weight:700;color:var(--white)}

/* app */
.app{position:absolute;top:3324px;left:0;width:1200px;height:542px}
.app-phone{position:absolute;left:115px;top:92px;width:285px;height:460px;background:var(--white);border-radius:26px 26px 0 0;box-shadow:0 4px 16px rgba(0,0,0,.14);overflow:hidden}
.app-phone-screen{position:absolute;left:16px;top:64px;width:253px;height:400px;background:linear-gradient(180deg,#44505c 0 28%,#f6f6f6 28% 60%,#dfe3e6 60%)}
.app .section-title{position:absolute;left:483px;top:146px;font-size:46px;white-space:nowrap}
.app p{position:absolute;left:483px;width:606px;font-size:17px;line-height:28px;text-align:justify;color:var(--text)}
.store-badge{position:absolute;top:410px;height:56px;background:#111;border-radius:7px}

/* footer */
.site-footer{position:absolute;top:3866px;left:0;width:1200px;height:420px;background:var(--dark);color:var(--white)}
.footer-brand{position:absolute;left:110px;top:180px;display:flex;align-items:center;gap:14px}
.footer-brand .brand-mark{width:52px;height:52px;background:var(--white)}
.footer-brand span{font-size:54px;font-weight:700;letter-spacing:2px}
.footer-col{position:absolute;top:100px}
.footer-col h5{font-size:22px;font-weight:700;margin-bottom:14px;letter-spacing:.5px}
.footer-col li{list-style:none;font-size:17px;line-height:33px}
.email-field{width:292px;height:50px;border:2px solid var(--white);margin-top:6px;font-size:16px;display:flex;align-items:center;padding-left:12px}
.subscribe-btn{margin-top:14px;width:134px;height:50px;background:var(--green);color:var(--ink);font-size:17px;display:flex;align-items:center;justify-content:center}
.footer-rule{position:absolute;left:110px;top:318px;width:980px;height:1px;background:#555}
.copyright{position:absolute;left:0;width:1200px;top:370px;text-align:center;font-size:16px}
</style>
</head>
<body>

<header class="site-header">
  <div class="brand"><span class="brand-mark"></span><span class="brand-name">Vexora</span></div>
  <div class="contact-item" style="left:640px">
    <svg width="20" height="36" viewBox="0 0 20 36"><rect x="2" y="1" width="16" height="34" rx="3" fill="none" stroke="#95c94a" stroke-width="2"/><circle cx="10" cy="30" r="1.8" fill="#95c94a"/></svg>
    <div><small>PHONE:</small><strong>+1 555 014 2270</strong></div>
  </div>
  <div class="contact-item" style="left:825px">
    <svg width="32" height="24" viewBox="0 0 32 24" style="margin-top:8px"><rect x="1" y="1" width="30" height="22" fill="none" stroke="#95c94a" stroke-width="2"/><path d="M1 1l15 12L31 1" fill="none" stroke="#95c94a" stroke-width="2"/></svg>
    <div><small>MAIL:</small><strong>hello@vexora.app</strong></div>
  </div>
  <nav class="main-nav">
    <a class="active" style="left:0">HOME</a>
    <a style="left:101px">PRICING</a>
    <a style="left:221px">SIGN UP</a>
    <a style="left:339px">CONTACT US</a>
    <a style="left:499px">ABOUT</a>
  </nav>
</header>

<section class="hero" role="img" aria-label="Photo of a businessman on a phone call, with blue-green gradient overlay">
  <h1>The Only Path You Want</h1>
  <p>Vexora is built to help anyone sort through the confusion of taking an idea</p>
  <a class="btn-outline">Read More</a>
</section>

<section class="about">
  <h2 class="section-title"><span class="b">What Is </span><span class="g">Vexora?</span></h2>
  <h3>Value Proposition</h3>
  <p style="top:206px">Mobile application that allows you to incorporate, set up legal structure, and use basic templates to get off the ground taking your idea to a real business.</p>
  <p style="top:312px">All encompassing platform to establish yourself legally and form a corporation that can stand the test of time.</p>
  <a class="btn blue" style="left:112px;top:400px;width:136px">Get Started</a>
  <a class="btn green" style="left:257px;top:400px;width:137px">Learn More</a>
  <div class="about-art" role="img" aria-label="Illustration of a man seen from behind under hand-drawn intellectual property doodles"></div>
</section>

<section class="services">
  <h2 class="vertical-title section-title"><span class="b">What We </span><span class="g">Provide..</span></h2>
  <div class="tablet"><div class="tablet-screen"><span>VEXORA</span></div></div>
  <div class="phone"><div class="phone-screen" role="img" aria-label="Landing page preview on a phone"></div></div>

  <article class="card" style="top:82px">
    <svg width="46" height="54" viewBox="0 0 46 54"><rect x="2" y="2" width="32" height="44" rx="2" fill="none" stroke="#3fb1f2" stroke-width="2"/><path d="M9 14h18M9 21h18M9 28h10" stroke="#3fb1f2" stroke-width="2"/><circle cx="32" cy="40" r="11" fill="#fff" stroke="#95c94a" stroke-width="2"/><path d="M27 40l4 4 7-7" fill="none" stroke="#95c94a" stroke-width="2"/></svg>
    <h4>Legal Structure</h4>
    <p>Decide which way you want to incorporate.</p>
    <a style="top:130px">Read More &gt;&gt;</a>
  </article>
  <article class="card" style="top:287px">
    <svg width="46" height="54" viewBox="0 0 46 54"><rect x="2" y="2" width="30" height="42" rx="2" fill="none" stroke="#3fb1f2" stroke-width="2"/><path d="M9 14h16M9 21h16" stroke="#3fb1f2" stroke-width="2"/><rect x="22" y="30" width="22" height="18" rx="3" fill="#fff" stroke="#95c94a" stroke-width="2"/><path d="M22 38h22" stroke="#95c94a" stroke-width="2"/></svg>
    <h4>Key Documents</h4>
    <p>Basic NDA, SOW, and other important document templates you can create.</p>
    <a style="top:145px">Read More &gt;&gt;</a>
  </article>
  <article class="card" style="top:493px">
    <svg width="46" height="54" viewBox="0 0 46 54"><circle cx="20" cy="20" r="13" fill="none" stroke="#3fb1f2" stroke-width="2"/><path d="M14 34h12v8H14z" fill="none" stroke="#3fb1f2" stroke-width="2"/><circle cx="34" cy="38" r="9" fill="#fff" stroke="#95c94a" stroke-width="2"/><path d="M34 33v10" stroke="#95c94a" stroke-width="2"/></svg>
    <h4>Connections</h4>
    <p>Algorithm connects you with the right lawyer to move forward.</p>
    <a style="top:145px">Read More &gt;&gt;</a>
  </article>
</section>

<section class="pricing">
  <h2 class="section-title"><span class="b">Subscription </span><span class="g">Model Packages</span></h2>
  <p class="lead">Mobile application that allows you to incorporate, set up legal structure, and use basic templates to get off the ground taking your idea to a real business.</p>

  <div class="plan silver" style="left:111px">
    <div class="plan-head">SILVER</div>
    <div class="price">$2.99</div>
    <ul><li>Nemo enim ipsam voluptatem</li><li>Magni dolores eos qui ratione</li><li>Neque porro quisquam</li><li>Sed quia non numquam eius</li><li>Tempora incidunt</li></ul>
    <a class="cta">START NOW</a>
  </div>
  <div class="plan gold">
    <div class="plan-head">GOLD</div>
    <div class="price">$4.99</div>
    <ul><li>Nemo enim ipsam voluptatem</li><li>Magni dolores eos qui ratione</li><li>Neque porro quisquam</li><li>Sed quia non numquam eius</li><li>Tempora incidunt</li></ul>
    <a class="cta">START NOW</a>
  </div>
  <div class="plan platinum" style="left:785px">
    <div class="plan-head">PLATINUM</div>
    <div class="price">$9.99</div>
    <ul><li>Nemo enim ipsam voluptatem</li><li>Magni dolores eos qui ratione</li><li>Neque porro quisquam</li><li>Sed quia non numquam eius</li><li>Tempora incidunt</li></ul>
    <a class="cta">START NOW</a>
  </div>
</section>

<section class="stats" role="img" aria-label="Workspace photo behind a blue-to-green gradient">
  <h2>Individual Proprietorships</h2>
  <p class="intro">Mobile application that allows you to incorporate, set up legal structure, and use basic templates to get off the ground taking your idea to a real business.</p>
  <div class="count">51,250,550</div>
  <p class="outro">We are here to help make the incorporation, idea protection and any other legal necessities an after thought for you.</p>
  <div class="stats-badge"><span>Vexora</span></div>
</section>

<section class="app">
  <div class="app-phone"><div class="app-phone-screen" role="img" aria-label="Landing page preview on a phone"></div></div>
  <h2 class="section-title"><span class="b">Also Available </span><span class="g">On Your Phone</span></h2>
  <p style="top:224px">Nemo enim ipsam voluptatem quia voluptas sit aspernatur aut odit aut fugit, sed quia consequuntur magni dolores eos qui ratione voluptatem sequi nesciunt.</p>
  <p style="top:314px">Quis autem vel eum iure reprehenderit qui in ea voluptate velit esse quam nihil molestiae consequatur.</p>
  <div class="store-badge" style="left:484px;width:187px" role="img" aria-label="Mobile download badge"></div>
  <div class="store-badge" style="left:684px;width:186px" role="img" aria-label="Mobile download badge"></div>
</section>

<footer class="site-footer">
  <div class="footer-brand"><span class="brand-mark"></span><span>VEXORA</span></div>
  <div class="footer-col" style="left:470px">
    <h5>QUICK LINKS</h5>
    <ul><li>Home</li><li>Pricing</li><li>Sign Up</li><li>Contact</li><li>About</li></ul>
  </div>
  <div class="footer-col" style="left:658px">
    <h5>LINKS</h5>
    <ul><li>Support</li><li>Blog</li><li>Press</li><li>Privacy</li><li>Terms</li></ul>
  </div>
  <div class="footer-col" style="left:795px">
    <h5>EMAIL SUBSCRIPTION</h5>
    <div class="email-field">Enter Your Email</div>
    <div class="subscribe-btn">Subscribe</div>
  </div>
  <div class="footer-rule"></div>
  <p class="copyright">Copyrights @ 2020 Vexora. All Rights Reserved.</p>
</footer>

</body>
</html>
```